Marlow Fern Beauty Co.- Label template for Australian Small Batch Skincare company

Marlow Fern is a small batch, locally made, hand crafted beauty company which makes natural, ethically sourced beauty products for socially conscious consumers.
I need someone to design a product label template that have certain fields empty for example; ingredients, instructions, batch # and product name. I want to be able to fill these fields in later because I make a lot of products, and need flexibility. I want this as a template so I can fill in these fields before sending to printer.
I need two different label sizes;
-60ml amber jar. Internal Dimensions 5.5cm including lid x 50mm round diameter.
-30ml amber jar. Internal dimensions 5cm including lid x 40mm round diameter
Colour of Label: Either rose gold or white font. Depending on what looks the best. On Black background.
Target Market(s)
I am a professional working woman, wife and mother. I use products that are work for me and contain pure ingredients. I try to live a healthy lifestyle and I like products that support this.Financially secure women. Professionals. Might have own business. Majority are full time workers. $80k plus. Urban dwellers. Clean living supporters. Use organics. Have healthy diets. Mothers whose children are 10 years +.
Industry/Entity Type
Skin Care Product
Font styles to use
Other font styles liked:
- Typo (typewriter look font)
Requirements
Must have
- product label template that have certain fields empty for example; ingredients, instructions, batch # and product name. I want to be able to fill these fields in later because I make a lot of products, and need flexibility. I want this as a template so I can fill in these fields before sending to printer.
- Logo
- Ingredients- Blank field
- Space for Product name- Blank field
- Space for Product description – Blank field
- Space for Instructions- Blank field.
- Batch number (and a blank field for filling out later)
- 60 or 30 ml
- Tagline – nurturing kind hearts, fierce minds, & brave spirits
- Hand crafted with love in Melbourne
- Website- www.marlowfernbeautycompany.example
- Black background, Rose gold font. Typo font. (Font that looks like typewriter)
Nice to have
- Art Deco design elements. Rose gold on black background. I want this label to represent my artisan approach to skin care formulation and production. Everything is handmade by me.
Should not have
- Mass production feel

```html
<!DOCTYPE html>
<html lang="en">
<head>
<meta charset="utf-8">
<title>Marlow Fern Beauty Co. – 60 ml Label Template</title>
<link rel="stylesheet" href="https://fonts.googleapis.com/css2?family=Zilla+Slab:wght@400;500&family=Oswald:wght@500&display=swap">
<style>
  :root {
    --page: #ffffff;
    --label-black: #000000;
    --rose-gold: #e4b19c;
    --rose-light: #f7dccf;
    --rose-deep: #c98d7a;
    --ink-white: #ffffff;
  }
  * { margin: 0; padding: 0; box-sizing: border-box; }
  html, body {
    width: 1200px;
    height: 800px;
    overflow: hidden;
    background: var(--page);
  }
  .canvas {
    position: relative;
    width: 1200px;
    height: 800px;
    font-family: "Zilla Slab", Georgia, serif;
    color: var(--ink-white);
  }
  .label {
    position: absolute;
    left: 53px;
    top: 118px;
    width: 1096px;
    height: 541px;
    background: var(--label-black);
  }
  .pattern-field {
    position: absolute;
    left: 73px;
    top: 2px;
    width: 956px;
    height: 537px;
    background: linear-gradient(135deg, var(--rose-light) 0%, var(--rose-gold) 45%, var(--rose-deep) 100%);
  }
  .content-panel {
    position: absolute;
    left: 199px;
    top: 34px;
    width: 700px;
    height: 408px;
    background: var(--label-black);
    border-radius: 60px 60px 18px 18px;
    box-shadow: 0 4px 10px rgba(0,0,0,0.35);
  }
  .panel-frame {
    position: absolute;
    inset: 0;
    width: 100%;
    height: 100%;
  }
  .brand-name {
    position: absolute;
    left: 0;
    right: 0;
    top: 124px;
    text-align: center;
    font-size: 28px;
    font-weight: 500;
    color: var(--rose-gold);
    letter-spacing: 1px;
  }
  .field {
    position: absolute;
    left: 0;
    right: 0;
    text-align: center;
    font-weight: 400;
    white-space: nowrap;
  }
  .field-ingredients { top: 216px; font-size: 14.5px; }
  .field-product-name { top: 248px; font-size: 25px; letter-spacing: 0.5px; }
  .field-description { top: 309px; font-size: 18px; line-height: 20px; }
  .tag-box {
    position: absolute;
    background: var(--label-black);
    border: 2px solid var(--rose-gold);
    font-family: "Oswald", "Arial Narrow", sans-serif;
    font-weight: 500;
    font-size: 20px;
    color: var(--ink-white);
    display: flex;
    align-items: center;
  }
  .batch-box { left: 133px; top: 475px; width: 133px; height: 49px; padding-left: 10px; }
  .volume-box { left: 507px; top: 483px; width: 85px; height: 41px; justify-content: center; font-size: 19px; }
  .side-text {
    position: absolute;
    font-size: 14px;
    line-height: 20px;
    white-space: nowrap;
    text-align: center;
  }
  .side-left {
    left: 38px;
    top: 274px;
    transform: translate(-50%, -50%) rotate(90deg);
  }
  .side-right {
    left: 1061px;
    top: 272px;
    transform: translate(-50%, -50%) rotate(-90deg);
  }
</style>
</head>
<body>
<main class="canvas">
  <section class="label">
    <div class="pattern-field" role="img" aria-label="Rose gold Art Deco braided leaf pattern on black"></div>

    <div class="content-panel">
      <svg class="panel-frame" viewBox="0 0 700 408" preserveAspectRatio="none" aria-hidden="true">
        <path d="M40 80 Q40 40 90 40 L610 40 Q660 40 660 80 L660 370 Q660 385 645 385 L55 385 Q40 385 40 370 Z"
              fill="none" stroke="var(--rose-gold)" stroke-width="2"/>
        <line x1="90" y1="376" x2="610" y2="376" stroke="var(--rose-light)" stroke-width="1.5"/>
      </svg>
      <div class="brand-name">Marlow Fern Beauty Co.</div>
      <p class="field field-ingredients">Ingredients Ingredients Ingredients Ingredients</p>
      <h1 class="field field-product-name" style="font-weight:400">PRODUCT NAME</h1>
      <p class="field field-description">Product description: product description roduct description<br>Instructions:&nbsp; instructions &nbsp; instructions &nbsp; instructions</p>
    </div>

    <div class="tag-box batch-box">BATCH #</div>
    <div class="tag-box volume-box">60 ml</div>

    <p class="side-text side-left">Hand crafted with love in Melbourne<br>www.marlowfernbeautycompany.example</p>
    <p class="side-text side-right">Nurturing kind hearts, fierce minds &amp; brave spirits.</p>
  </section>
</main>
</body>
</html>
```